zQuandaro Marketing - SEM, Influencer website. FUN RETRO VIBES.

I included content. Need an advertising website that displays, my services, blog and about me and contact.
I need to be able to easily update content, blogs by myself. Need it to be a Wordpress. I included some content pages. Please let me know if this give a better idea of what I do and the tone I am looking for.
Target Market(s)
Small Business Entrepreneurs, Start-ups, Male and Female ages 25-50
Industry/Entity Type
Advertising
Coding
Coded - Design and coding required
Number of Pages Required
3 page
Font styles to use
Other font styles liked:
- Lazer 64
Requirements
Must have
- Services, Blog, About Me, Contact. Creative Design is really what I want. Unique and fun imagery. I like the 80's style of design. Retro colors, in the logo. LAzer 84 font is cool. Hex colors should be in the brief. MUST LOOK GOOD ON MOBILE. The mobile experience has to be good.
Nice to have
- I am open minded to new creative ideas.
Hex Code
#000205
#3978A3
#5BF8FB
#7B7BFB
#5CC9EC
#AB63FA
Should not have
- Cookie Cutter feel. They made me choose the color wheel but the colors I want are on the brief. Please let me know if you need more logo images, images of me

```html
<!DOCTYPE html>
<html lang="en">
<head>
<meta charset="utf-8">
<title>zQuandaro Marketing</title>
<link rel="stylesheet" href="https://fonts.googleapis.com/css2?family=Montserrat:wght@600;700;800&family=Open+Sans:wght@400;600;700&family=Permanent+Marker&display=swap">
<style>
  :root {
    --ink: #000205;
    --deep-blue: #3978A3;
    --aqua: #5BF8FB;
    --periwinkle: #7B7BFB;
    --sky: #5CC9EC;
    --violet: #AB63FA;
    --band-purple: #8d6cc8;
    --hero-grey: #5a5868;
    --white: #ffffff;
    --subscribe-bg: #3b3b3b;
    --field-bg: #262626;
    --footer-bg: #1b1b1b;
    --footer-rule: #444444;
  }
  * { box-sizing: border-box; margin: 0; padding: 0; }
  html, body { width: 1200px; height: 3346px; overflow: hidden; }
  body { position: relative; background: var(--white); font-family: "Open Sans", Arial, sans-serif; color: var(--ink); }
  a { color: inherit; text-decoration: none; }

  /* Header + hero */
  .hero { position: absolute; left: 0; top: 0; width: 1200px; height: 799px; }
  .hero-photo { position: absolute; left: 0; top: 0; width: 1200px; height: 799px;
    background: linear-gradient(90deg, #86d6f0 0%, #9fd9f1 35%, #a8b4ea 70%, #a592dc 100%); }
  .hero-cap { position: absolute; left: 0; top: 0; width: 1200px; height: 260px; }
  .brand { position: absolute; left: 58px; top: 52px; display: flex; align-items: center; gap: 12px;
    font-family: "Open Sans", Arial, sans-serif; font-weight: 700; font-size: 30px; color: var(--periwinkle); }
  .brand-dot { width: 26px; height: 26px; border-radius: 50%; background: var(--periwinkle); }
  .main-nav { position: absolute; top: 34px; right: 76px; display: flex; gap: 52px;
    font-family: "Montserrat", Arial, sans-serif; font-weight: 700; font-size: 15px; color: var(--ink); }
  .hero-copy { position: absolute; left: 0; top: 350px; width: 1200px; text-align: center; }
  .hero-kicker { font-family: "Montserrat", Arial, sans-serif; font-weight: 800; font-size: 32px; letter-spacing: 1px; color: var(--hero-grey); line-height: 42px; }
  .hero-title { font-family: "Permanent Marker", cursive; font-size: 58px; color: var(--white); line-height: 66px; letter-spacing: 1px; }
  .hero-text { width: 620px; margin: 30px auto 0; font-size: 14.5px; font-weight: 600; line-height: 19px; color: var(--ink); }
  .slider-dots { position: absolute; top: 722px; left: 466px; display: flex; gap: 13px; }
  .slider-dots span { width: 81px; height: 7px; background: var(--white); }
  .slider-dots .active { background: linear-gradient(90deg, var(--violet), var(--sky)); }

  /* Services */
  .services { position: absolute; left: 0; top: 799px; width: 1200px; height: 497px;
    background: linear-gradient(90deg, var(--band-purple) 0%, var(--sky) 50%, var(--band-purple) 100%); color: var(--white); }
  .section-title { font-family: "Open Sans", Arial, sans-serif; font-weight: 700; font-size: 26px; text-align: center; letter-spacing: 1px; }
  .services .section-title { position: absolute; top: 30px; width: 100%; }
  .service { position: absolute; top: 112px; width: 290px; text-align: center; }
  .service-icon { width: 140px; height: 140px; margin: 0 auto; border-radius: 16px; background: rgba(255,255,255,0.28); }
  .service-name { margin-top: 42px; font-weight: 700; font-size: 17px; }
  .service-text { margin-top: 18px; font-size: 12.5px; line-height: 15.5px; font-weight: 600; }
  .slider-arrow { position: absolute; top: 188px; }

  /* Blog */
  .blog { position: absolute; left: 0; top: 1296px; width: 1200px; height: 566px; background: var(--white); }
  .blog .section-title { position: absolute; top: 42px; width: 100%; color: var(--ink); }
  .blog-video { position: absolute; left: 45px; top: 158px; width: 606px; height: 371px; }
  .video-still { position: absolute; inset: 0; background: linear-gradient(135deg, #3a2a22 0%, #7a5238 45%, #2e2420 100%); }
  .video-controls { position: absolute; left: 0; bottom: 0; width: 606px; height: 44px; background: rgba(0,0,0,0.55); }
  .blog-post { position: absolute; left: 698px; top: 152px; width: 440px; }
  .post-title { font-family: "Permanent Marker", cursive; font-size: 34px; line-height: 40px; color: var(--ink); }
  .post-text { margin-top: 12px; font-size: 16.5px; line-height: 20.5px; }
  .post-text + .post-text { margin-top: 20px; }

  /* About */
  .about { position: absolute; left: 0; top: 1862px; width: 1200px; height: 893px;
    background: linear-gradient(90deg, var(--band-purple) 0%, var(--sky) 38%, var(--sky) 50%, var(--band-purple) 100%); color: var(--white); }
  .portrait { position: absolute; left: 67px; top: 183px; width: 446px; height: 446px; border-radius: 50%; overflow: hidden;
    background: radial-gradient(circle at 50% 40%, #2a2a2a 0 30%, #111 31%), var(--white); }
  .portrait-fill { width: 100%; height: 100%; background: linear-gradient(180deg, var(--white) 0%, var(--white) 45%, #1a1a1a 75%, var(--ink) 100%); }
  .owner-name { position: absolute; left: 0; top: 640px; width: 580px; text-align: center; font-family: "Permanent Marker", cursive; font-size: 34px; color: var(--white); line-height: 40px; }
  .owner-role { position: absolute; left: 0; top: 688px; width: 580px; text-align: center; font-size: 15px; color: var(--ink); }
  .milestone { position: absolute; left: 580px; width: 580px; }
  .milestone-icon { position: absolute; left: 0; top: 10px; width: 120px; height: 120px; border-radius: 14px; background: rgba(255,255,255,0.25); }
  .milestone-body { position: absolute; left: 196px; top: 0; width: 360px; }
  .milestone-title { font-weight: 700; font-size: 26px; line-height: 32px; }
  .milestone-text { margin-top: 6px; font-size: 12.5px; line-height: 15.5px; height: 78px; overflow: hidden; }
  .read-more { position: absolute; left: 557px; top: 2675px; font-size: 15px; color: var(--white); border-bottom: 1px solid var(--white); padding-bottom: 2px; }

  /* Subscribe */
  .subscribe { position: absolute; left: 0; top: 2755px; width: 1200px; height: 241px; background: var(--subscribe-bg); }
  .email-field { position: absolute; left: 384px; top: 82px; width: 435px; height: 60px; background: var(--field-bg);
    color: #4a4a4a; font-size: 17px; padding: 18px 22px; }
  .subscribe-btn { position: absolute; left: 500px; top: 165px; width: 200px; height: 35px; border: 2px solid var(--periwinkle);
    color: var(--white); font-size: 17px; text-align: center; line-height: 31px; }

  /* Footer */
  .site-footer { position: absolute; left: 0; top: 2996px; width: 1200px; height: 350px; background: var(--footer-bg); color: var(--white); }
  .footer-brand { position: absolute; left: 82px; top: 128px; display: flex; align-items: center; gap: 12px; font-weight: 700; font-size: 30px; color: var(--periwinkle); }
  .footer-col { position: absolute; top: 62px; }
  .footer-col h3 { font-family: "Montserrat", Arial, sans-serif; font-weight: 700; font-size: 20px; margin-bottom: 14px; }
  .footer-col li { list-style: none; font-size: 17.5px; line-height: 35px; }
  .contact-list li { display: flex; align-items: flex-start; gap: 14px; }
  .contact-list svg { margin-top: 10px; flex: none; }
  .social { position: absolute; left: 1025px; top: 237px; display: flex; gap: 10px; }
  .social span { width: 22px; height: 22px; background: var(--white); border-radius: 3px; }
  .footer-rule { position: absolute; left: 80px; top: 287px; width: 1053px; height: 1px; background: var(--footer-rule); }
  .copyright { position: absolute; left: 80px; top: 312px; font-size: 13px; font-weight: 600; }
</style>
</head>
<body>

<header class="hero">
  <div class="hero-photo" role="img" aria-label="Soft blue and violet toned photo of a person holding a tablet with sales figures"></div>
  <svg class="hero-cap" width="1200" height="260" viewBox="0 0 1200 260" aria-hidden="true">
    <path d="M0 0 H1200 V87 H300 C238 87 236 170 160 208 C110 234 50 250 0 257 Z" fill="#ffffff"/>
  </svg>
  <a class="brand" href="#"><span class="brand-dot"></span>zQuandaro</a>
  <nav class="main-nav">
    <a href="#">HOME</a><a href="#">BLOG</a><a href="#">SERVICES</a><a href="#">ABOUT</a><a href="#">CONTACT</a>
  </nav>
  <div class="hero-copy">
    <p class="hero-kicker">USE YOUR</p>
    <h1 class="hero-title">ADVERTISING DOLLARS</h1>
    <p class="hero-kicker">EFFICIENTLY AND EFFECTIVELY.</p>
    <p class="hero-text">Lorem ipsum dolor sit amet, consectetur adipiscing elit, sed do eiusmod tempor incididunt ut labore et dolore magna aliqua. Ut enim ad minim veniam, quis nostrud exercitation ullamco laboris nisi ut aliquip ex ea commodo consequat.</p>
  </div>
  <div class="slider-dots"><span class="active"></span><span></span><span></span></div>
</header>

<section class="services">
  <h2 class="section-title">SERVICES</h2>
  <svg class="slider-arrow" style="left:30px" width="50" height="100" viewBox="0 0 50 100" aria-hidden="true"><path d="M44 4 L8 50 L44 96" fill="none" stroke="#ffffff" stroke-opacity="0.6" stroke-width="5"/></svg>
  <svg class="slider-arrow" style="left:1120px" width="50" height="100" viewBox="0 0 50 100" aria-hidden="true"><path d="M6 4 L42 50 L6 96" fill="none" stroke="#ffffff" stroke-opacity="0.6" stroke-width="5"/></svg>
  <div class="service" style="left:87px">
    <div class="service-icon" role="img" aria-label="Icon of a hand ticking a checklist clipboard"></div>
    <h3 class="service-name">Planning &amp; Proposal Services</h3>
    <p class="service-text">Lorem ipsum dolor sit amet, consectetur adipiscing elit, sed do eiusmod tempor incididunt ut labore et dolore magna aliqua. Quis ipsum suspendisse ultrices gravida. Risus commodo viverra maecenas accumsan lacus vel facilisis.</p>
  </div>
  <div class="service" style="left:453px">
    <div class="service-icon" role="img" aria-label="Icon of a magnifier over a target with an arrow"></div>
    <h3 class="service-name">SEM Services</h3>
    <p class="service-text">Lorem ipsum dolor sit amet, consectetur adipiscing elit, sed do eiusmod tempor incididunt ut labore et dolore magna aliqua. Quis ipsum suspendisse ultrices gravida. Risus commodo viverra maecenas accumsan lacus vel facilisis.</p>
  </div>
  <div class="service" style="left:814px">
    <div class="service-icon" role="img" aria-label="Icon of a megaphone surrounded by media symbols"></div>
    <h3 class="service-name">Campaign Management</h3>
    <p class="service-text">Lorem ipsum dolor sit amet, consectetur adipiscing elit, sed do eiusmod tempor incididunt ut labore et dolore magna aliqua. Quis ipsum suspendisse ultrices gravida. Risus commodo viverra maecenas accumsan lacus vel facilisis.</p>
  </div>
</section>

<section class="blog">
  <h2 class="section-title">BLOG</h2>
  <div class="blog-video">
    <div class="video-still" role="img" aria-label="Video still of friends gathered at a warmly lit bar"></div>
    <svg style="position:absolute;left:230px;top:108px" width="146" height="146" viewBox="0 0 146 146" aria-hidden="true">
      <circle cx="73" cy="73" r="70" fill="none" stroke="#ffffff" stroke-width="3"/>
      <path d="M55 38 L112 73 L55 108 Z" fill="#ffffff"/>
    </svg>
    <div class="video-controls">
      <svg width="606" height="44" viewBox="0 0 606 44" aria-hidden="true">
        <path d="M18 13 L34 22 L18 31 Z" fill="#ffffff"/>
        <path d="M70 18 H76 L84 12 V32 L76 26 H70 Z" fill="#ffffff"/>
        <g fill="#9aa8ff"><rect x="106" y="14" width="3" height="16"/><rect x="114" y="14" width="3" height="16"/><rect x="122" y="14" width="3" height="16"/><rect x="130" y="14" width="3" height="16"/><rect x="138" y="14" width="3" height="16"/><rect x="146" y="14" width="3" height="16"/></g>
        <g fill="#ffffff"><circle cx="568" cy="22" r="4"/><circle cx="584" cy="13" r="4"/><circle cx="584" cy="31" r="4"/></g>
        <path d="M568 22 L584 13 M568 22 L584 31" stroke="#ffffff" stroke-width="2"/>
      </svg>
    </div>
  </div>
  <article class="blog-post">
    <h3 class="post-title">LOREM IPSUM</h3>
    <p class="post-text">Lorem ipsum dolor sit amet, consectetur adipiscing elit, sed do eiusmod tempor incididunt ut labore et dolore magna aliqua. Quis ipsum suspendisse ultrices gravida. Risus commodo viverra maecenas accumsan lacus vel facilisis.</p>
    <p class="post-text">Lorem ipsum dolor sit amet, consectetur adipiscing elit, sed do eiusmod tempor incididunt ut labore et dolore magna aliqua. Quis ipsum suspendisse ultrices gravida. Risus commodo viverra maecenas accumsan lacus vel facilisis.</p>
  </article>
</section>

<section class="about">
  <div class="portrait"><div class="portrait-fill" role="img" aria-label="Portrait placeholder for the business owner"></div></div>
  <p class="owner-name">YOUR NAME</p>
  <p class="owner-role">JOB TITLE</p>

  <div class="milestone" style="top:104px">
    <div class="milestone-icon" role="img" aria-label="Icon of a figure climbing stairs"></div>
    <div class="milestone-body">
      <h3 class="milestone-title">In the beginning .....</h3>
      <p class="milestone-text">My digital business passion started right after I graduated from college. I worked for an e-commerce business, it was a small but thriving. It generated up to $100,000 per month with 1 product and little overhead. I can recall precisely receiving email alerts each time a sale</p>
    </div>
  </div>
  <div class="milestone" style="top:285px">
    <div class="milestone-icon" role="img" aria-label="Icon of a glowing light bulb"></div>
    <div class="milestone-body">
      <h3 class="milestone-title">Newbie Entrepreneur</h3>
      <p class="milestone-text">I took the jump! With only $200.00 to buy inventory, I started developing my e-commerce brand with 0 marketing budget. My first year in business I generated $25,000 in sales only using free online tools. Talk about a challenge, I learned a lot about what to do and</p>
    </div>
  </div>
  <div class="milestone" style="top:466px">
    <div class="milestone-icon" role="img" aria-label="Icon of a businessman pointing forward"></div>
    <div class="milestone-body">
      <h3 class="milestone-title">Corporate life</h3>
      <p class="milestone-text">That's when I got a call from a recruiter for a Searchwell Agency Account Strategist. This career move is what changed my knowledge level from entry-level to expert. As an account strategist, I worked with a book of Searchwell Partnered agencies assigned to me for the pur-</p>
    </div>
  </div>
  <div class="milestone" style="top:635px">
    <div class="milestone-icon" role="img" aria-label="Icon of an eye inside a focus frame"></div>
    <div class="milestone-body">
      <h3 class="milestone-title">Developing &nbsp;the Vision........</h3>
      <p class="milestone-text">With the help of God, I started to write the vision. How can I use the skills that I have acquired throughout the years to help others to succeed. There is a gap in the industry, where small business struggle to adapt technology and start to fail behind in the quickly evolving digi-</p>
    </div>
  </div>
</section>
<a class="read-more" href="#">Read More</a>

<section class="subscribe">
  <div class="email-field">Your Email</div>
  <a class="subscribe-btn" href="#">SUBSCRIBE</a>
</section>

<footer class="site-footer">
  <div class="footer-brand"><span class="brand-dot"></span>zQuandaro</div>
  <div class="footer-col" style="left:433px">
    <h3>NAVIGATE</h3>
    <ul><li>HOME</li><li>SERVICES</li><li>BLOG</li><li>ABOUT</li><li>CONTACT</li></ul>
  </div>
  <div class="footer-col" style="left:627px">
    <h3>CONTACT</h3>
    <ul class="contact-list">
      <li><svg width="16" height="16" viewBox="0 0 16 16" aria-hidden="true"><path d="M3 1 L6 1 L7 5 L5 6.5 C6 9 7 10 9.5 11 L11 9 L15 10 L15 13 C15 14 14 15 13 15 C6 14 2 10 1 3 C1 2 2 1 3 1 Z" fill="#ffffff"/></svg>000 000 0000</li>
      <li><svg width="18" height="14" viewBox="0 0 18 14" aria-hidden="true"><rect x="0" y="0" width="18" height="14" fill="#ffffff"/><path d="M0 0 L9 8 L18 0" fill="none" stroke="#1b1b1b" stroke-width="1.5"/></svg>hello@zquandaro.test</li>
      <li><svg width="14" height="18" viewBox="0 0 14 18" aria-hidden="true"><path d="M7 0 C3 0 0 3 0 7 C0 12 7 18 7 18 C7 18 14 12 14 7 C14 3 11 0 7 0 Z" fill="#ffffff"/><circle cx="7" cy="7" r="2.5" fill="#1b1b1b"/></svg>Address, City<br>ST 0000</li>
    </ul>
  </div>
  <div class="footer-col" style="left:890px">
    <h3>LEGAL</h3>
    <ul><li>Terms&amp;Conditions</li><li>Private Policies</li><li>Testimonials</li></ul>
  </div>
  <div class="social" aria-label="Social links"><span></span><span></span><span></span></div>
  <div class="footer-rule"></div>
  <p class="copyright">2020 @copyright, zQuandaro</p>
</footer>

</body>
</html>
```